Korvell Plant Services

We are a heavy diesel mechanical business with additional air con certificates, remapping engine rebuilt

Contact Information for Business Card

Company Name, Director Name, Managing Director, Contact details, email and website

Font styles to use
Serif
Script

```html
<!DOCTYPE html>
<html lang="en">
<head>
<meta charset="utf-8">
<title>Korvell Plant Services – Business Card</title>
<link href="https://fonts.googleapis.com/css2?family=Arimo:wght@400;700&display=swap" rel="stylesheet">
<style>
  :root {
    --page-bg: #e4e5e8;
    --card-bg: #ffffff;
    --navy: #2b3585;
    --navy-dark: #1f2766;
    --ink: #111111;
    --grey-text: #555a66;
  }
  * { box-sizing: border-box; margin: 0; padding: 0; }
  html, body {
    width: 1200px; height: 900px; overflow: hidden;
    background: var(--page-bg);
    font-family: "Arimo", Arial, sans-serif;
  }
  .stage { position: relative; width: 1200px; height: 900px; }
  .card {
    position: absolute; left: 250px;
    width: 700px; height: 400px;
    background: var(--card-bg);
    overflow: hidden;
    box-shadow: 0 6px 18px rgba(0,0,0,0.18);
  }
  .card--front { top: 30px; }
  .card--back { top: 470px; }
  .ridge-band {
    position: absolute; left: 0; top: 0; width: 700px; height: 400px;
  }
  .brand {
    position: absolute; right: 40px; top: 70px;
    display: flex; align-items: center; gap: 12px;
  }
  .brand__dot {
    width: 26px; height: 26px; border-radius: 50%;
    background: var(--navy);
  }
  .brand__name {
    font-weight: 700; font-size: 30px; line-height: 1.05;
    color: var(--navy); width: 190px;
  }
  .website-line {
    position: absolute; left: 46px; top: 78px;
    font-size: 17px; font-weight: 700; letter-spacing: 4px;
    color: var(--ink);
  }
  .website-line .domain { color: var(--navy); }
  .person { position: absolute; left: 46px; top: 112px; }
  .person__name {
    font-size: 24px; font-weight: 700; color: var(--navy-dark);
  }
  .person__role {
    font-size: 17px; color: var(--grey-text); margin-top: 4px;
  }
  .address {
    position: absolute; left: 66px; top: 186px;
    font-size: 17px; font-style: normal; line-height: 1.25; color: var(--grey-text);
  }
  .contacts {
    position: absolute; left: 66px; top: 268px;
    list-style: none;
  }
  .contacts li {
    display: flex; align-items: center; gap: 10px;
    font-size: 17px; line-height: 1.45; color: var(--grey-text);
  }
  .contacts svg { width: 15px; height: 15px; fill: var(--navy); flex: none; }
</style>
</head>
<body>
<main class="stage">

  <section class="card card--front">
    <svg class="ridge-band" viewBox="0 0 700 400" preserveAspectRatio="none" aria-hidden="true">
      <path fill="var(--navy)" d="M0 372 L60 366 L110 352 L160 348 L210 330 L250 318 L300 314 L350 296 L390 286 L430 264 L470 248 L510 244 L550 226 L590 216 L630 190 L670 178 L700 170 L700 400 L0 400 Z"/>
    </svg>
    <p class="website-line">www.<span class="domain">korvellplant</span>.net</p>
    <div class="brand">
      <span class="brand__dot"></span>
      <span class="brand__name">Korvell Plant Services</span>
    </div>
  </section>

  <section class="card card--back">
    <svg class="ridge-band" viewBox="0 0 700 400" preserveAspectRatio="none" aria-hidden="true">
      <path fill="var(--navy)" d="M0 384 L80 382 L160 380 L240 376 L310 372 L350 356 L390 334 L430 314 L470 298 L510 280 L550 266 L590 250 L630 236 L670 226 L700 218 L700 400 L0 400 Z"/>
    </svg>
    <div class="brand">
      <span class="brand__dot"></span>
      <span class="brand__name">Korvell Plant Services</span>
    </div>
    <div class="person">
      <h1 class="person__name">DALE MERRIN</h1>
      <p class="person__role">Managing Director</p>
    </div>
    <address class="address">
      48 Tarrant Road<br>
      Hollowfield<br>
      WA 6091, Australia
    </address>
    <ul class="contacts">
      <li>
        <svg viewBox="0 0 24 24" aria-hidden="true"><path d="M6.6 10.8a15 15 0 0 0 6.6 6.6l2.2-2.2c.3-.3.7-.4 1-.2 1.1.4 2.3.6 3.6.6.6 0 1 .4 1 1V20c0 .6-.4 1-1 1A17 17 0 0 1 3 4c0-.6.4-1 1-1h3.5c.6 0 1 .4 1 1 0 1.3.2 2.5.6 3.6.1.3 0 .7-.2 1z"/></svg>
        0412 384 906
      </li>
      <li>
        <svg viewBox="0 0 24 24" aria-hidden="true"><path d="M2 5h20v14H2zM4 7v.4l8 5 8-5V7l-8 5z"/></svg>
        admin@korvellplant.net
      </li>
      <li>
        <svg viewBox="0 0 24 24" aria-hidden="true"><path d="M12 2a10 10 0 1 0 0 20 10 10 0 0 0 0-20zm6.9 9h-3a15 15 0 0 0-1.3-5.6A8 8 0 0 1 18.9 11zM12 4c.9 1.2 1.8 3.6 1.9 7h-3.8C10.2 7.6 11.1 5.2 12 4zM9.4 5.4A15 15 0 0 0 8.1 11h-3a8 8 0 0 1 4.3-5.6zM5.1 13h3a15 15 0 0 0 1.3 5.6A8 8 0 0 1 5.1 13zm6.9 7c-.9-1.2-1.8-3.6-1.9-7h3.8c-.1 3.4-1 5.8-1.9 7zm2.6-1.4a15 15 0 0 0 1.3-5.6h3a8 8 0 0 1-4.3 5.6z"/></svg>
        www.korvellplant.net
      </li>
    </ul>
  </section>

</main>
</body>
</html>
```